Resume/CV/Cover Letter templates

We are a career management business and are starting to offer tailored career documents. we want 3-4 styles/themes with resume and cover letter templates. I have some examples to show you that are a good starting point (but are someone else's IP). see attached files

Target Market(s)

Corporate

Font styles to use
Sans Serif

Requirements
Must have
• Clean lines. Simple formatting. Corporate look and feel. Not too busy.
• Matching resume and cover letter documents
Nice to have
• One Blue theme
• One Green theme
• One other
Should not have
• too much jazziness!

```html
<!DOCTYPE html>
<html lang="en">
<head>
<meta charset="utf-8">
<title>Resume Template – Blue Theme</title>
<link rel="stylesheet" href="https://fonts.googleapis.com/css2?family=Carlito:wght@400;700&display=swap">
<style>
  :root{
    --backdrop:#616163;
    --paper:#f2f2f2;
    --cyan:#00aeef;
    --cyan-light:#3cc1f1;
    --cyan-pale:#7fd6f6;
    --heading:#14a4e0;
    --icon:#1f4f97;
    --ink:#1a1a1a;
    --track:#a6a6a6;
    --rule:#ffffff;
  }
  *{box-sizing:border-box;margin:0;padding:0}
  html,body{width:1200px;height:1000px;overflow:hidden;background:var(--backdrop)}
  body{position:relative;font-family:"Carlito","Calibri",sans-serif;color:var(--ink)}
  .page{position:absolute;top:276px;width:373px;height:482px;background:var(--paper);overflow:hidden}
  .page--one{left:33px}
  .page--two{left:416px}
  .page--three{left:797px}
  .abs{position:absolute}
  .header-shape,.footer-shape{position:absolute;left:0;top:0}
  .name{position:absolute;left:46px;top:31px;font-size:30px;color:#fff;letter-spacing:.3px;font-weight:400;line-height:1}
  .name b{font-weight:700}
  .contact{position:absolute;left:255px;top:20px;list-style:none}
  .contact li{display:flex;align-items:center;height:13px;font-size:6px;color:#fff;letter-spacing:.2px}
  .contact svg{margin-right:4px}
  .section-title{position:absolute;display:flex;align-items:center;font-size:9px;color:var(--heading);height:12px}
  .section-title svg{margin-right:5px;flex:none}
  .text{position:absolute;font-size:6px;line-height:8.8px}
  .entry{position:absolute;font-size:6px;line-height:8.8px}
  .entry-title{font-weight:700;font-size:6.3px;margin-bottom:1px}
  .career{position:absolute;left:50px;top:310px;width:293px;border-collapse:collapse;font-size:5.5px}
  .career th{background:var(--cyan);color:#fff;font-weight:400;text-align:left;height:15px;padding-left:3px;border-right:2px solid var(--paper)}
  .career td{height:12.6px;padding-left:3px;color:#444;border-bottom:1px solid var(--rule);border-right:2px solid var(--paper);background:#ececec}
  .page-number{position:absolute;right:22px;top:444px;font-size:6px}
  .page-number--pale{color:#7fd0f0}
  .skill{position:absolute;display:flex;align-items:center;font-size:6px;height:8px}
  .skill span{width:50px}
  .bar{position:relative;width:99px;height:4px;background:var(--track)}
  .bar i{position:absolute;left:0;top:0;bottom:0;width:71%;background:var(--cyan)}
  .row{position:absolute;display:flex;font-size:6px}
</style>
</head>
<body>

<!-- Page 1 -->
<section class="page page--one">
  <svg class="header-shape" width="373" height="105" viewBox="0 0 373 105">
    <polygon points="0,0 373,0 373,95 0,100" fill="var(--cyan)"/>
    <polygon points="130,0 373,0 373,40" fill="var(--cyan-light)"/>
    <polygon points="200,60 373,30 373,95" fill="var(--cyan-light)"/>
    <polygon points="0,70 240,56 0,100" fill="var(--cyan-light)" opacity=".7"/>
    <line x1="12" y1="92" x2="328" y2="73" stroke="#fff" stroke-width="1.2"/>
  </svg>
  <h1 class="name">YOUR <b>NAME</b></h1>
  <ul class="contact">
    <li><svg width="9" height="9"><circle cx="4.5" cy="4.5" r="4.5" fill="#fff"/><circle cx="4.5" cy="4" r="1.5" fill="var(--cyan)"/></svg>ADDRESS</li>
    <li><svg width="9" height="9"><circle cx="4.5" cy="4.5" r="4.5" fill="#fff"/><rect x="3" y="2.5" width="3" height="4" rx="1" fill="var(--cyan)"/></svg>TELEPHONE</li>
    <li><svg width="9" height="9"><circle cx="4.5" cy="4.5" r="4.5" fill="#fff"/><rect x="2.3" y="3" width="4.4" height="3" fill="var(--cyan)"/></svg>MAIL ADDRESS</li>
    <li><svg width="9" height="9"><circle cx="4.5" cy="4.5" r="4.5" fill="#fff"/><circle cx="4.5" cy="4.5" r="2" fill="none" stroke="var(--cyan)" stroke-width=".8"/></svg>WEB ADDRESS</li>
  </ul>

  <h2 class="section-title" style="left:32px;top:108px"><svg width="12" height="12"><circle cx="6" cy="6" r="6" fill="var(--icon)"/><circle cx="6" cy="4.5" r="1.8" fill="#fff"/><path d="M3 9 Q6 5.5 9 9Z" fill="#fff"/></svg>PROFILE</h2>
  <p class="text" style="left:50px;top:126px;width:295px">Lorem ipsum dolor sit amet, consectetur adipiscing elit. In id elementum diam. Nulla et tincidunt erat. Nunc vel nisl a tortor posuere tempus. Class aptent taciti sociosqu ad litora torquent per conubia nostra, per inceptos himenaeos. Lorem ipsum dolor sit amet, consectetur adipiscing elit. In id elementum diam. Nulla et tincidunt erat. Nunc vel nisl a tortor posuere tempus. Class aptent taciti sociosqu ad litora torquent per conubia nostra, per inceptos himenaeos.</p>

  <h2 class="section-title" style="left:32px;top:175px"><svg width="12" height="12"><circle cx="6" cy="6" r="6" fill="var(--icon)"/><path d="M2 5.5 L6 3.5 L10 5.5 L6 7.5Z" fill="#fff"/></svg>Education</h2>
  <div class="entry" style="left:50px;top:192px;width:295px"><p class="entry-title">Degree name &nbsp;|&nbsp; University name 2000-2001</p><p>Lorem ipsum dolor sit amet, consectetur adipiscing elit. In id elementum diam. Nulla et tincidunt erat. Nunc vel nisl a tortor posuere tempus.</p></div>
  <div class="entry" style="left:50px;top:224px;width:295px"><p class="entry-title">Degree name &nbsp;|&nbsp; University name 2000-2001</p><p>Lorem ipsum dolor sit amet, consectetur adipiscing elit. In id elementum diam. Nulla et tincidunt erat. Nunc vel nisl a tortor posuere tempus.</p></div>
  <div class="entry" style="left:50px;top:256px;width:295px"><p class="entry-title">Degree name &nbsp;|&nbsp; University name 2000-2001</p><p>Lorem ipsum dolor sit amet, consectetur adipiscing elit. In id elementum diam. Nulla et tincidunt erat. Nunc vel nisl a tortor posuere tempus.</p></div>

  <h2 class="section-title" style="left:32px;top:293px"><svg width="12" height="12"><circle cx="6" cy="6" r="6" fill="var(--icon)"/><circle cx="6.5" cy="3" r="1.1" fill="#fff"/><path d="M6 4.5 L5 7 L3 9.5 M5 7 L7.5 9.5 M4 5.5 L8 5" stroke="#fff" stroke-width=".9" fill="none"/></svg>Career Summary</h2>
  <table class="career">
    <thead><tr><th style="width:77px">DATES</th><th style="width:107px">POSITION</th><th>ORGANISATION</th></tr></thead>
    <tbody>
      <tr><td>[Date] to [Date]</td><td>[Position]</td><td>[Organisation]</td></tr>
      <tr><td>[Date] to [Date]</td><td>[Position]</td><td>[Organisation]</td></tr>
      <tr><td>[Date] to [Date]</td><td>[Position]</td><td>[Organisation]</td></tr>
      <tr><td>[Date] to [Date]</td><td>[Position]</td><td>[Organisation]</td></tr>
      <tr><td>[Date] to [Date]</td><td>[Position]</td><td>[Organisation]</td></tr>
      <tr><td>[Date] to [Date]</td><td>[Position]</td><td>[Organisation]</td></tr>
    </tbody>
  </table>
  <p class="page-number">Page | 1</p>
</section>

<!-- Page 2 -->
<section class="page page--two">
  <h2 class="section-title" style="left:31px;top:31px"><svg width="12" height="12"><circle cx="6" cy="6" r="6" fill="var(--icon)"/><rect x="3" y="4.5" width="6" height="4" rx=".6" fill="#fff"/><rect x="4.8" y="3.3" width="2.4" height="1.4" fill="none" stroke="#fff" stroke-width=".6"/></svg>Professional Experience</h2>
  <div class="entry" style="left:49px;top:48px;width:298px"><p class="entry-title">Job title here 2000 – 2001 &nbsp;|&nbsp; Company name</p><p>Lorem ipsum dolor sit amet, consectetur adipiscing elit. In id elementum diam. Nulla et tincidunt erat. Nunc vel nisl a tortor posuere tempus. Class aptent taciti sociosqu ad litora torquent per conubia nostra, per inceptos himenaeos</p></div>
  <div class="entry" style="left:49px;top:89px;width:298px"><p class="entry-title">Job title here 2000 – 2001 &nbsp;|&nbsp; Company name</p><p>Lorem ipsum dolor sit amet, consectetur adipiscing elit. In id elementum diam. Nulla et tincidunt erat. Nunc vel nisl a tortor posuere tempus. Class aptent taciti sociosqu ad litora torquent per conubia nostra, per inceptos himenaeos</p></div>
  <div class="entry" style="left:49px;top:130px;width:298px"><p class="entry-title">Job title here 2000 – 2001 &nbsp;|&nbsp; Company name</p><p>Lorem ipsum dolor sit amet, consectetur adipiscing elit. In id elementum diam. Nulla et tincidunt erat. Nunc vel nisl a tortor posuere tempus. Class aptent taciti sociosqu ad litora torquent per conubia nostra, per inceptos himenaeos</p></div>
  <div class="entry" style="left:49px;top:171px;width:298px"><p class="entry-title">Job title here 2000 – 2001 &nbsp;|&nbsp; Company name</p><p>Lorem ipsum dolor sit amet, consectetur adipiscing elit. In id elementum diam. Nulla et tincidunt erat. Nunc vel nisl a tortor posuere tempus. Class aptent taciti sociosqu ad litora torquent per conubia nostra, per inceptos himenaeos</p></div>
  <div class="entry" style="left:49px;top:212px;width:298px"><p class="entry-title">Job title here 2000 – 2001 &nbsp;|&nbsp; Company name</p><p>Lorem ipsum dolor sit amet, consectetur adipiscing elit. In id elementum diam. Nulla et tincidunt erat. Nunc vel nisl a tortor posuere tempus. Class aptent taciti sociosqu ad litora torquent per conubia nostra, per inceptos himenaeos</p></div>
  <div class="entry" style="left:49px;top:253px;width:298px"><p class="entry-title">Job title here 2000 – 2001 &nbsp;|&nbsp; Company name</p><p>Lorem ipsum dolor sit amet, consectetur adipiscing elit. In id elementum diam. Nulla et tincidunt erat. Nunc vel nisl a tortor posuere tempus. Class aptent taciti sociosqu ad litora torquent per conubia nostra, per inceptos himenaeos</p></div>
  <div class="entry" style="left:49px;top:294px;width:298px"><p class="entry-title">Job title here 2000 – 2001 &nbsp;|&nbsp; Company name</p><p>Lorem ipsum dolor sit amet, consectetur adipiscing elit. In id elementum diam. Nulla et tincidunt erat. Nunc vel nisl a tortor posuere tempus. Class aptent taciti sociosqu ad litora torquent per conubia nostra, per inceptos himenaeos</p></div>

  <h2 class="section-title" style="left:31px;top:349px"><svg width="12" height="12"><circle cx="6" cy="6" r="6" fill="var(--icon)"/><path d="M3.5 3.5 L6 8.5 L8.5 3.5" stroke="#fff" stroke-width="1.2" fill="none"/></svg>Professional Skills</h2>
  <div class="skill" style="left:49px;top:367px"><span>Experience 01</span><div class="bar"><i></i></div></div>
  <div class="skill" style="left:49px;top:381px"><span>Experience 02</span><div class="bar"><i></i></div></div>
  <div class="skill" style="left:49px;top:394px"><span>Experience 03</span><div class="bar"><i></i></div></div>
  <div class="skill" style="left:49px;top:408px"><span>Experience 04</span><div class="bar"><i></i></div></div>
  <div class="skill" style="left:49px;top:421px"><span>Experience 05</span><div class="bar"><i></i></div></div>
  <p class="page-number">Page | 2</p>
</section>

<!-- Page 3 -->
<section class="page page--three">
  <h2 class="section-title" style="left:31px;top:22px"><svg width="12" height="12"><circle cx="6" cy="6" r="6" fill="var(--icon)"/><circle cx="6" cy="5.2" r="2.4" fill="#fff"/><rect x="5" y="7.3" width="2" height="1.8" fill="#fff"/></svg>Personal Skills</h2>
  <div class="skill" style="left:49px;top:40px"><span>Experience 01</span><div class="bar"><i></i></div></div>
  <div class="skill" style="left:49px;top:54px"><span>Experience 02</span><div class="bar"><i></i></div></div>
  <div class="skill" style="left:49px;top:67px"><span>Experience 03</span><div class="bar"><i></i></div></div>
  <div class="skill" style="left:49px;top:81px"><span>Experience 04</span><div class="bar"><i></i></div></div>
  <div class="skill" style="left:49px;top:95px"><span>Experience 05</span><div class="bar"><i></i></div></div>

  <h2 class="section-title" style="left:31px;top:114px"><svg width="12" height="12"><circle cx="6" cy="6" r="6" fill="var(--icon)"/><rect x="3" y="3" width="6" height="3.5" fill="#fff"/><rect x="4" y="6.5" width="1" height="3" fill="#fff"/></svg>Training</h2>
  <div class="entry" style="left:49px;top:131px"><p>Training 01 &nbsp;&nbsp;&nbsp;&nbsp;&nbsp;&nbsp;2000 – 2001</p><p>Lorem ipsum dolor sit amet, consectetur adipiscing elit.</p></div>
  <div class="entry" style="left:49px;top:153px"><p>Training 01 &nbsp;&nbsp;&nbsp;&nbsp;&nbsp;&nbsp;2000 – 2001</p><p>Lorem ipsum dolor sit amet, consectetur adipiscing elit.</p></div>
  <div class="entry" style="left:49px;top:175px"><p>Training 01 &nbsp;&nbsp;&nbsp;&nbsp;&nbsp;&nbsp;2000 – 2001</p><p>Lorem ipsum dolor sit amet, consectetur adipiscing elit.</p></div>

  <h2 class="section-title" style="left:31px;top:204px"><svg width="12" height="12"><circle cx="6" cy="6" r="6" fill="var(--icon)"/><circle cx="6" cy="7" r="2.2" fill="#fff"/><path d="M4.5 2.5 L6 4.8 L7.5 2.5" stroke="#fff" stroke-width=".9" fill="none"/></svg>Awards</h2>
  <p class="text" style="left:49px;top:222px">Award you won 2000</p>
  <p class="text" style="left:49px;top:235px">Award you won 2000</p>
  <p class="text" style="left:49px;top:249px">Award you won 2000</p>
  <p class="text" style="left:49px;top:262px">Award you won 2000</p>

  <h2 class="section-title" style="left:31px;top:276px"><svg width="12" height="12"><circle cx="6" cy="6" r="6" fill="var(--icon)"/><circle cx="6" cy="6" r="3" fill="none" stroke="#fff" stroke-width=".9"/><path d="M3 6 H9" stroke="#fff" stroke-width=".7"/></svg>Language</h2>
  <p class="text" style="left:49px;top:294px">English</p>
  <p class="text" style="left:113px;top:294px">Spanish</p>
  <p class="text" style="left:170px;top:294px">Dutch</p>
  <p class="text" style="left:225px;top:294px">Chinese</p>

  <h2 class="section-title" style="left:31px;top:314px"><svg width="12" height="12"><circle cx="6" cy="6" r="6" fill="var(--icon)"/><path d="M3.5 8.5 Q4 3 8.5 3.5 Q6 5 5.5 8.5Z" fill="#fff"/></svg>Hobbies</h2>
  <p class="text" style="left:49px;top:331px">Games</p>
  <p class="text" style="left:115px;top:331px">Reading</p>
  <p class="text" style="left:171px;top:331px">Designing</p>
  <p class="text" style="left:225px;top:331px">Riding</p>

  <svg class="footer-shape" width="373" height="482" viewBox="0 0 373 482">
    <polygon points="0,409 180,444 0,482" fill="var(--cyan-light)"/>
    <polygon points="0,450 373,418 373,482 0,482" fill="var(--cyan)" opacity=".9"/>
    <polygon points="0,460 180,444 90,482 0,482" fill="var(--cyan-light)" opacity=".7"/>
  </svg>
  <p class="page-number page--three-number page-number--pale">Page | 3</p>
</section>

</body>
</html>
```